DIGITAL MENUS

Hi Odette (This project is for Odette ONLY)Hope you are well. Can you please help me with designing a new menu for me.I've attached my current menu for you. I would like a new layout using photos for each items.You can use same photos as the menu board that you have designed for me before.Layout must be in Landscape form as current menu. JPEG files.

Need extra days to review

• Hi Odette,
• Ideal layout:
• DISPLAY MENU #1:
• Rice paper Rolls and Spring rolls
• Pho
• DISPLAY MENU #2:
• Noodle Salads
• Rice
• Stirfry Noodles
• DISPLAY MENU #3:
• Drinks
• 1. All soft drinks $3
• 2. Cape Harrowby water $3
• 3. T. Varsenzo Sparkling water $4.5
• 4. Zestora Water $4.5
• 5. Harbek Ice-Tea $4.5
• 6. Pulpwell Juices $5
• 7. Kombucha $5
• and Vietnamese Drinks

```html
<!DOCTYPE html>
<html lang="en">
<head>
<meta charset="utf-8">
<title>Display Menu 2 – Noodle Salads, Rice, Stirfry Noodles</title>
<link rel="stylesheet" href="https://fonts.googleapis.com/css2?family=Stint+Ultra+Expanded&family=Libre+Baskerville:ital@1&display=swap">
<style>
  :root {
    --board: #0b0606;
    --board-deep: #140808;
    --ink: #ffffff;
    --divider: #ffffff;
    --dish-dark: #6b4a34;
    --dish-mid: #b98a5a;
    --dish-light: #d8b98e;
  }
  * { margin: 0; padding: 0; box-sizing: border-box; }
  html, body { width: 1200px; height: 673px; overflow: hidden; background: var(--board); }
  .menu-board {
    position: relative;
    width: 1200px;
    height: 673px;
    overflow: hidden;
    background: linear-gradient(135deg, var(--board-deep), var(--board));
  }
  .feature-dish { position: absolute; inset: 0; width: 1200px; height: 673px; }
  .menu-section { position: absolute; left: 643px; width: 538px; }
  .section-head {
    display: flex;
    justify-content: space-between;
    align-items: baseline;
    font-family: "Stint Ultra Expanded", serif;
    color: var(--ink);
    font-size: 26px;
    line-height: 1;
    text-shadow: 1px 1px 0 #000;
  }
  .section-rule {
    margin-top: 8px;
    height: 0;
    border-top: 3px dotted var(--ink);
  }
  .dish-list { list-style: none; margin-top: 10px; }
  .dish-list li {
    font-family: "Libre Baskerville", serif;
    font-style: italic;
    color: var(--ink);
    font-size: 28px;
    line-height: 40.5px;
    white-space: nowrap;
  }
  .noodle-salads { top: 22px; }
  .rice { top: 258px; }
  .stirfry-noodles { top: 494px; }
</style>
</head>
<body>
<main class="menu-board">
  <svg class="feature-dish" viewBox="0 0 1200 673" aria-hidden="false">
    <defs>
      <radialGradient id="dishTone" cx="0.45" cy="0.5" r="0.6">
        <stop offset="0" stop-color="var(--dish-light)"/>
        <stop offset="0.55" stop-color="var(--dish-mid)"/>
        <stop offset="1" stop-color="var(--dish-dark)"/>
      </radialGradient>
    </defs>
    <polygon points="615,0 627,0 571,673 559,673" fill="var(--divider)"/>
    <polygon points="0,0 615,0 559,673 0,673" fill="url(#dishTone)" role="img" aria-label="Photo of a pan of stir-fried rice noodles with beef strips, broccoli, red peppers and carrots"/>
  </svg>

  <section class="menu-section noodle-salads">
    <h2 class="section-head"><span>Noodle Salads</span><span>$13.50</span></h2>
    <div class="section-rule"></div>
    <ul class="dish-list">
      <li>Lemongrass Beef</li>
      <li>Lemongrass Chicken</li>
      <li>Bbq Pork</li>
      <li>Tofu</li>
    </ul>
  </section>

  <section class="menu-section rice">
    <h2 class="section-head"><span>Rice</span><span>$15.50</span></h2>
    <div class="section-rule"></div>
    <ul class="dish-list">
      <li>Bbq Beef</li>
      <li>Lemongrass Chilli Chicken</li>
      <li>Tofu &amp; Vegs</li>
      <li>Fried Rice</li>
    </ul>
  </section>

  <section class="menu-section stirfry-noodles">
    <h2 class="section-head"><span>Stirfry Noodles</span><span>$15.50</span></h2>
    <div class="section-rule"></div>
    <ul class="dish-list">
      <li>Beef</li>
      <li>Chicken</li>
      <li>Tofu</li>
    </ul>
  </section>
</main>
</body>
</html>
```